KESTREL: Flu Social Media Post #2

- Please create a similar design to the one attached to create a Social Media Post image.
- Attached, Logo, boarder, sample flu social media image.
- KESTREL - must be included
- Flu - must be included
- Protect your community. Protect Your Elders. Stay Vaccinated. - must be included
- image of mom/daughter holding hands must be included
- For inspiration, https://quelmoda.org/, and https://www.facebook.com/Quelmoda

```html
<!DOCTYPE html>
<html lang="en">
<head>
<meta charset="utf-8">
<title>KESTREL – Flu Social Media Post</title>
<link rel="stylesheet" href="https://fonts.googleapis.com/css2?family=Barlow:wght@500;800;900&family=Barlow+Semi+Condensed:wght@400;500&display=swap">
<style>
  :root {
    --teal: #4aa3ac;
    --brick: #b55a50;
    --cream: #fcefde;
    --band: #fdfaf4;
    --frame-a: #5e9ea4;
    --frame-b: #9a8f8c;
    --frame-c: #b0655c;
  }
  html, body {
    margin: 0;
    padding: 0;
    width: 1200px;
    height: 1200px;
    overflow: hidden;
    background: #ffffff;
  }
  .post {
    position: relative;
    width: 1200px;
    height: 1200px;
    overflow: hidden;
    font-family: "Barlow", sans-serif;
  }
  .frame-pattern {
    position: absolute;
    inset: 0;
    background: linear-gradient(135deg, var(--frame-a) 0%, var(--frame-b) 50%, var(--frame-c) 100%);
    opacity: 0.85;
  }
  .panel {
    position: absolute;
    left: 37px;
    top: 37px;
    width: 1126px;
    height: 1126px;
    background: var(--cream);
  }
  .photo {
    position: absolute;
    left: 50px;
    top: 490px;
    width: 1110px;
    height: 673px;
    background:
      radial-gradient(ellipse 28% 60% at 24% 60%, rgba(110, 60, 110, 0.55), transparent 70%),
      radial-gradient(ellipse 26% 60% at 80% 62%, rgba(40, 30, 30, 0.6), transparent 70%),
      linear-gradient(180deg, rgba(70, 60, 60, 0.35) 0%, rgba(180, 120, 90, 0.35) 100%);
  }
  .title-box {
    position: absolute;
    left: 83px;
    top: 83px;
    width: 772px;
    height: 172px;
    border: 7px solid var(--teal);
    display: flex;
    align-items: center;
    justify-content: center;
  }
  .title {
    margin: 0;
    font-family: "Barlow", sans-serif;
    font-weight: 500;
    font-size: 170px;
    line-height: 1;
    letter-spacing: 4px;
    color: var(--brick);
    transform: translateY(4px);
  }
  .org-name {
    position: absolute;
    left: 895px;
    top: 120px;
    width: 220px;
    margin: 0;
    font-family: "Barlow Semi Condensed", sans-serif;
    font-weight: 500;
    font-size: 30px;
    line-height: 1.1;
    color: var(--teal);
    text-transform: uppercase;
    text-align: center;
  }
  .band {
    position: absolute;
    left: 40px;
    width: 1123px;
    display: flex;
    align-items: center;
    justify-content: center;
    box-shadow: 0 4px 6px rgba(60, 40, 30, 0.35);
    font-weight: 900;
    white-space: nowrap;
  }
  .band .lead { color: var(--brick); }
  .band .key { color: var(--teal); margin-left: 0.25em; }
  .band-community {
    top: 385px;
    height: 133px;
    background: rgba(253, 250, 244, 0.96);
    font-size: 86px;
  }
  .band-elders {
    top: 562px;
    height: 134px;
    background: rgba(255, 255, 255, 0.72);
    font-size: 86px;
  }
  .band-vaccinated {
    top: 746px;
    height: 133px;
    background: rgba(255, 255, 255, 0.6);
    font-size: 124px;
  }
  .cta {
    position: absolute;
    left: 33px;
    top: 1031px;
    width: 1130px;
    height: 90px;
    background: #ffffff;
    display: flex;
    align-items: center;
    justify-content: center;
    margin: 0;
    font-family: "Barlow Semi Condensed", sans-serif;
    font-weight: 400;
    font-size: 42px;
    letter-spacing: 1.5px;
    color: var(--teal);
  }
</style>
</head>
<body>
  <main class="post">
    <div class="frame-pattern" role="img" aria-label="Woven zigzag border pattern in teal, grey and red"></div>
    <section class="panel"></section>
    <div class="photo" role="img" aria-label="Photo of a mother and daughter seen from behind, holding hands, wearing embroidered blouses"></div>

    <div class="title-box">
      <h1 class="title">KESTREL</h1>
    </div>
    <p class="org-name">Northern Circle Elder Alliance</p>

    <div class="band band-community"><span class="lead">Protect</span><span class="key">Your Community.</span></div>
    <div class="band band-elders"><span class="lead">Protect</span><span class="key">Your Elders.</span></div>
    <div class="band band-vaccinated"><span class="lead">Stay</span><span class="key">Vaccinated.</span></div>

    <p class="cta">Learn more about getting vaccinated against the Flu</p>
  </main>
</body>
</html>
```